Brannock Bay Ferry and Haulage

Need to redesign our business cards to relay that we do freight logistics and water taxi service. We also work with gov. agencies doing environmental clean up, oil spill response, remote site construction and work with many of the air taxi and helicopter services on Kodiak Island. Out website is www.brannockbayferry.com to get a better idea of what we do.

Contact Information for Business Card

I have a previous business card but it just has the logo on the front, and a sunset picture on the back with the contact info. It does not relay what we do and what we can help with. I like a simple straight forward design over a busy one.

Colors
3176b5
0455a3
cfdfed

Requirements
Must have
• logo, email, website, phone number

```html
<!DOCTYPE html>
<html lang="en">
<head>
<meta charset="utf-8">
<title>Brannock Bay Ferry and Haulage – Business Card</title>
<link href="https://fonts.googleapis.com/css2?family=Exo+2:wght@700&family=Lato:wght@400&display=swap" rel="stylesheet">
<style>
  :root {
    --card-blue: #0b3ec4;
    --card-blue-deep: #0936ad;
    --text-white: #ffffff;
    --text-light: #7fb6ee;
    --accent-orange: #f4a21c;
    --page-bg: #e9edf2;
    --divider: rgba(255,255,255,0.35);
  }
  * { box-sizing: border-box; margin: 0; padding: 0; }
  html, body { width: 1200px; height: 782px; overflow: hidden; }
  body {
    background: var(--page-bg);
    display: flex;
    flex-direction: column;
    align-items: center;
    justify-content: center;
    gap: 30px;
    font-family: "Lato", Arial, sans-serif;
  }
  .card {
    width: 620px;
    height: 354px;
    background: var(--card-blue);
    box-shadow: 0 6px 18px rgba(0,0,0,0.18);
  }

  /* Back side: photo grid */
  .card-back {
    padding: 14px;
    display: grid;
    grid-template-columns: repeat(3, 1fr);
    grid-template-rows: repeat(2, 1fr);
    gap: 8px;
  }
  .photo-tile { width: 100%; height: 100%; }
  .tile-a { background: linear-gradient(160deg, #c9d3dc, #6d6f70 60%, #3a3d40); }
  .tile-b { background: linear-gradient(170deg, #a9b8c6, #5b6b78 55%, #2f4350); }
  .tile-c { background: linear-gradient(165deg, #8fb4e0, #485561 55%, #2a3036); }
  .tile-d { background: linear-gradient(160deg, #d8dde2, #6b6258 55%, #2c2a28); }
  .tile-e { background: linear-gradient(170deg, #9ab3c8, #7a6a55 55%, #3a3430); }
  .tile-f { background: linear-gradient(165deg, #b9c6d8, #8c8576 55%, #3c3e40); }

  /* Front side */
  .card-front {
    display: flex;
    align-items: center;
    padding: 0 40px;
  }
  .brand {
    width: 270px;
    display: flex;
    align-items: center;
    gap: 12px;
  }
  .brand-dot {
    flex: none;
    width: 30px;
    height: 30px;
    border-radius: 50%;
    background: var(--accent-orange);
  }
  .brand-name {
    font-family: "Exo 2", Arial, sans-serif;
    font-weight: 700;
    font-size: 26px;
    line-height: 1.15;
    color: var(--text-white);
    text-transform: uppercase;
  }
  .divider {
    width: 1px;
    height: 190px;
    background: var(--divider);
    margin: 0 34px 0 18px;
  }
  .contact-block { color: var(--text-light); }
  .person-name {
    font-family: "Exo 2", Arial, sans-serif;
    font-weight: 700;
    font-size: 25px;
    letter-spacing: 1px;
    color: var(--text-white);
    text-transform: uppercase;
  }
  .person-title {
    font-size: 16px;
    margin: 2px 0 16px;
  }
  .contact-list { list-style: none; }
  .contact-item {
    display: flex;
    align-items: center;
    gap: 8px;
    font-size: 16px;
    line-height: 1.55;
  }
  .contact-icon { width: 14px; height: 14px; flex: none; fill: var(--accent-orange); }
</style>
</head>
<body>
  <section class="card card-back">
    <div class="photo-tile tile-a" role="img" aria-label="Photo of a work boat moored at a dock"></div>
    <div class="photo-tile tile-b" role="img" aria-label="Photo of an aluminium landing craft on the water"></div>
    <div class="photo-tile tile-c" role="img" aria-label="Photo of a boat carrying portable units"></div>
    <div class="photo-tile tile-d" role="img" aria-label="Photo of crew loading equipment on deck"></div>
    <div class="photo-tile tile-e" role="img" aria-label="Photo of a deck loaded with lumber freight"></div>
    <div class="photo-tile tile-f" role="img" aria-label="Photo of machinery being transported by boat"></div>
  </section>

  <section class="card card-front">
    <div class="brand">
      <span class="brand-dot"></span>
      <span class="brand-name">Brannock Bay Ferry and Haulage</span>
    </div>
    <div class="divider"></div>
    <div class="contact-block">
      <h1 class="person-name">Marcus Hale</h1>
      <p class="person-title">Managing Director</p>
      <ul class="contact-list">
        <li class="contact-item">
          <svg class="contact-icon" viewBox="0 0 24 24"><path d="M6.6 10.8a15 15 0 0 0 6.6 6.6l2.2-2.2a1 1 0 0 1 1-.25 11.4 11.4 0 0 0 3.6.57 1 1 0 0 1 1 1V20a1 1 0 0 1-1 1A17 17 0 0 1 3 4a1 1 0 0 1 1-1h3.5a1 1 0 0 1 1 1c0 1.25.2 2.45.57 3.57a1 1 0 0 1-.25 1z"/></svg>
          044-555 018 274
        </li>
        <li class="contact-item">
          <svg class="contact-icon" viewBox="0 0 24 24"><path d="M2 5h20v14H2z M2 5l10 8 10-8" fill="var(--accent-orange)"/><path d="M3 6l9 7 9-7" stroke="var(--card-blue)" stroke-width="2" fill="none"/></svg>
          info@brannockbayferry.com
        </li>
        <li class="contact-item">
          <svg class="contact-icon" viewBox="0 0 24 24"><circle cx="12" cy="12" r="10"/><path d="M2 12h20M12 2c3 3 3 17 0 20M12 2c-3 3-3 17 0 20" stroke="var(--card-blue)" stroke-width="1.6" fill="none"/></svg>
          www.brannockbayferry.com
        </li>
      </ul>
    </div>
  </section>
</body>
</html>
```